Create a business Card for a Women Owned Business Body Positive Company. The winner we hope to work with on other projects coming up for grand opening for flyers, postcards, email marketing, facebook page, stationary, labels, tshirt design....
We would like if possible in the background of the card a infinity symbol or crown if it fits into the design if not it's ok. But I am open to all suggestions we had alot problems with the our new logo being created this time sad to say :(

Our colors are Royal Purple, Grey, Black Thank you in advance for your talent, you hard work and your submissions!
Delia and Nadine :)
Updates

my Logo is velvet harbor boutique which is purple and has a heart and infinity sign in it and my colors are purple silver and black only of another card i had done nothing else. My logo is VELVET HARBOR BOUTIQUE LOGO

Industry/Entity Type

Retail

Contact Information for Business Card

website: www.velvtharborboutiques.example email: sales@velvetharborboutique.example
Delia Pruett & Nadine Kolb Owners

Font styles to use
Script

Colors
b768aa

Requirements
Must have
• COLORS ARE PURPLE BLACK AND GREY
Nice to have
• INFINITY SIGNING IN THE BACKGROUND

```html
<!DOCTYPE html>
<html lang="en">
<head>
<meta charset="utf-8">
<title>Velvet Harbor Boutique — Business Card</title>
<link rel="stylesheet" href="https://fonts.googleapis.com/css2?family=Cinzel:wght@400;600&family=Cormorant+Garamond:wght@500&family=Open+Sans:wght@400&display=swap">
<style>
  :root {
    --stage: #e9e7ec;
    --royal-purple: #7a47ab;
    --royal-purple-light: #8a58b8;
    --card-white: #fbfbfb;
    --ink-white: #ffffff;
    --ink-grey: #5e5e62;
    --rule-dark: #3a3a3e;
  }
  * { margin: 0; padding: 0; box-sizing: border-box; }
  html, body {
    width: 1200px; height: 886px; overflow: hidden;
    background: var(--stage);
  }
  .stage {
    position: relative; width: 1200px; height: 886px;
    display: flex; justify-content: center; align-items: center; gap: 70px;
  }
  .card {
    position: relative; width: 340px; height: 560px;
    border-radius: 26px;
    box-shadow: 0 14px 34px rgba(40, 20, 60, 0.18);
    overflow: hidden;
  }

  /* Contact side */
  .card--contact {
    background: linear-gradient(160deg, var(--royal-purple-light), var(--royal-purple));
    color: var(--ink-white);
  }
  .card__frame {
    position: absolute; inset: 16px;
    border: 1.5px solid var(--ink-white);
    border-radius: 18px;
  }
  .contact__block {
    position: absolute; top: 118px; left: 0; right: 0;
    text-align: center;
  }
  .contact__icon { display: block; margin: 0 auto 8px; }
  .contact__names {
    font-family: "Cinzel", serif; font-weight: 400;
    font-size: 23px; line-height: 1.1; letter-spacing: 0.5px;
  }
  .contact__role {
    font-family: "Cinzel", serif; font-size: 15px;
    letter-spacing: 1px; margin-top: 2px;
  }
  .contact__details {
    margin-top: 44px;
    font-family: "Cormorant Garamond", serif; font-weight: 500;
    font-size: 16.5px; line-height: 1.25;
  }
  .contact__line { display: block; }
  .contact__sep { display: block; margin: 8px auto 6px; }
  .ornament-area {
    position: absolute; left: 38px; right: 118px; bottom: 28px; height: 68px;
    background: linear-gradient(90deg, rgba(255,255,255,0.55), rgba(255,255,255,0.25));
    border-radius: 34px;
  }

  /* Brand side */
  .card--brand { background: var(--card-white); }
  .brand__mark {
    position: absolute; top: 205px; left: 0; right: 0;
    text-align: center;
  }
  .brand__name {
    font-family: "Cinzel", serif; font-weight: 400;
    font-size: 25px; line-height: 1.25; color: var(--royal-purple);
    letter-spacing: 0.5px;
  }
  .brand__rule {
    width: 240px; height: 1.5px; margin: 8px auto 0;
    background: var(--rule-dark);
  }
  .brand__web {
    position: absolute; bottom: 54px; left: 0; right: 0; text-align: center;
    font-family: "Open Sans", sans-serif; font-size: 12px;
    letter-spacing: 1.6px; color: var(--ink-grey);
  }
</style>
</head>
<body>
<main class="stage">
  <section class="card card--contact">
    <div class="card__frame"></div>
    <div class="contact__block">
      <svg class="contact__icon" width="18" height="18" viewBox="0 0 18 18" aria-hidden="true">
        <circle cx="9" cy="5" r="4" fill="#fff"/>
        <path d="M1 18c0-5 3.5-8 8-8s8 3 8 8z" fill="#fff"/>
      </svg>
      <p class="contact__names">Delia Pruett<br>Nadine Kolb</p>
      <p class="contact__role">owners</p>
      <div class="contact__details">
        <span class="contact__line">sales@velvetharborboutique.example</span>
        <svg class="contact__sep" width="14" height="10" viewBox="0 0 14 10" aria-hidden="true">
          <rect x="0.5" y="0.5" width="13" height="9" fill="#fff"/>
          <path d="M1 1l6 5 6-5" stroke="#7a47ab" fill="none"/>
        </svg>
        <span class="contact__line">velvtharborboutiques.example</span>
        <svg class="contact__sep" width="12" height="12" viewBox="0 0 12 12" aria-hidden="true">
          <circle cx="6" cy="6" r="5.5" fill="#fff"/>
          <path d="M0.5 6h11M6 0.5c-3 3-3 8 0 11M6 0.5c3 3 3 8 0 11" stroke="#7a47ab" fill="none" stroke-width="0.8"/>
        </svg>
      </div>
    </div>
    <div class="ornament-area" role="img" aria-label="Decorative scrollwork flourish in white"></div>
  </section>

  <section class="card card--brand">
    <div class="brand__mark">
      <p class="brand__name">Velvet Harbor<br>Boutique</p>
      <div class="brand__rule"></div>
    </div>
    <p class="brand__web">www.velvtharborboutiques.example</p>
  </section>
</main>
</body>
</html>
```